Ledgerwise Reach - B2B Demand Generation Website Project

We need a fully functional website for www.ledgerwisereach.example. We are a B2B Demand Generation company, based in London, working with companies such as QRT, VKD, Norvex, Brindlow, Tarvo generating them sales leads for their sales teams. We run this through digital marketing newsletter promotions and have a network of websites. Content syndication, data, demand generation, online marketing. Our logo has just been redone (attached) and we have a holding page already which i would like to use the style / colours. Our logo is bright and vibrant but i dont want the site to be a rainbow. We are expensive, classy, professorial, B2B, intelligent.

Home
About Us
Our Services
Prospora & QA Technology
Intent Data
Testimonials
Contact Us
Updates

Target Market(s)

B2B Marketers (QRT, Velquarion, Tarvo, VKD, Opal Reach, Driftmoor, Harlow Quantis, Technology Companies, Data Companies, Marketing Teams, Tumbleden.

Industry/Entity Type

Marketing

Coding

Coded - Design and coding required

Number of Pages Required

5+ page

Font styles to use
Sans Serif

Requirements
Must have
• Home
About Us
Our Services
Prospora & QA Technology
Intent Data
Testimonials
Contact Us

Simple Pages.

Look classy, intelligent, data experts. I like the video homepages were the image moves at the top. Very soft animation.
Nice to have
• Websites i like:

https://www.vkd.example/
https://www.brevantor.example/
https://www.plumfieldsites.example.co.uk/

Ledgerwise Reach - The Demand Generation Company
Should not have
• Glimpsevault crap images

```html
<!DOCTYPE html>
<html lang="en">
<head>
<meta charset="utf-8">
<title>Ledgerwise Reach - The Demand Generation Company</title>
<link href="https://fonts.googleapis.com/css2?family=Raleway:wght@400;500;600;700&family=Open+Sans:wght@400;600;700&display=swap" rel="stylesheet">
<style>
:root{
  --blue:#0d4d9a;
  --blue-deep:#0a3a78;
  --navy:#0e2f63;
  --red:#b01f21;
  --red-deep:#8f1414;
  --ink:#1c3f78;
  --grey:#777;
  --line:#c9d5ea;
  --white:#fff;
}
*{margin:0;padding:0;box-sizing:border-box}
html,body{width:1200px;height:3660px;overflow:hidden}
body{position:relative;font-family:'Open Sans',sans-serif;color:var(--grey);background:var(--white)}
.abs{position:absolute}
h1,h2,h3{font-family:'Raleway',sans-serif;font-weight:500}

/* top bar */
.topbar{left:0;top:0;width:1200px;height:35px;background:var(--blue);z-index:3}
.topbar-contact{right:70px;top:10px;font-size:11px;color:#dfe8f5}
.topbar-search{right:0;top:0;width:60px;height:35px;background:var(--blue-deep);display:flex;align-items:center;justify-content:center}

/* hero */
.hero-media{left:0;top:0;width:1200px;height:588px;background:linear-gradient(120deg,#4d4a4b 0%,#8b7f78 35%,#c9c3ba 60%,#9a8f87 85%,#6e625c 100%)}
.brand{left:22px;top:94px;display:flex;align-items:center;gap:8px}
.brand-dot{width:22px;height:22px;border-radius:50%;border:3px solid var(--red);display:block}
.brand-name{font-family:'Raleway',sans-serif;font-size:21px;color:var(--red);font-weight:500}
.brand-tag{left:44px;top:123px;font-size:7px;color:#fff;white-space:nowrap}
.nav{right:26px;top:92px;display:flex;gap:19px;font-size:14px;color:#fff}
.hero-kicker{left:155px;top:246px;font-family:'Raleway',sans-serif;font-size:21px;color:#fff}
.hero-title{left:155px;top:288px;font-size:33px;line-height:48px;color:#fff;font-weight:600;white-space:nowrap}
.btn-explore{left:156px;top:408px;width:155px;height:47px;background:#fff;color:var(--blue);font-size:15px;font-family:'Raleway',sans-serif;font-weight:600;display:flex;align-items:center;justify-content:center}

/* updates */
.updates{left:0;top:588px;width:1200px;height:88px;background:var(--red-deep)}
.updates-label{left:198px;top:36px;font-size:15px;color:#fff;font-weight:600;font-family:'Raleway',sans-serif}
.updates-msg{left:346px;top:0;width:728px;height:88px;background:var(--red);color:#fff;font-size:12px;display:flex;align-items:center;padding-left:44px}
.updates-msg b{margin-left:8px;font-weight:600}
.updates-arrows{left:1075px;top:0;width:125px;height:88px;display:flex;align-items:center;justify-content:space-around}

/* partners */
.partners{left:0;top:676px;width:1200px;height:213px;background:var(--blue)}
.partner-row{left:60px;top:60px;width:1080px;display:flex;justify-content:space-between}
.partner{display:flex;align-items:center;gap:7px;color:#b9cbe6;font-family:'Raleway',sans-serif;font-size:24px;font-weight:600;width:150px;justify-content:center}
.partner i{width:10px;height:10px;background:#b9cbe6;display:block}

/* stats */
.stats{left:156px;top:845px;width:888px;height:175px;background:#fff;border:1px solid var(--line);display:flex}
.stat{flex:1;text-align:center;border-right:1px dashed var(--line);padding-top:38px}
.stat:last-child{border-right:none}
.stat-label{font-size:17px;color:var(--ink);font-family:'Raleway',sans-serif}
.stat-num{font-size:46px;color:var(--red);font-family:'Raleway',sans-serif;font-weight:500;margin-top:18px}

/* welcome */
.welcome-title{left:155px;top:1255px;font-size:34px;color:var(--navy)}
.rule-red{height:3px;width:46px;background:var(--red)}
.welcome-rule{left:155px;top:1310px}
.welcome-text{left:155px;top:1333px;width:420px;font-size:12.5px;line-height:20px;color:#888}
.welcome-frame-out{left:716px;top:1075px;width:462px;height:484px;border:1px solid #7d9ed1}
.welcome-media{left:629px;top:1100px;width:524px;height:507px;background:linear-gradient(135deg,#6c6a66 0%,#a9a197 40%,#c6b79f 70%,#7c6d5a 100%)}
.welcome-frame-in{left:650px;top:1130px;width:478px;height:457px;border:1px solid var(--red)}
.welcome-play{left:876px;top:1328px}

/* services */
.services-title{left:0;top:1688px;width:1200px;text-align:center;font-size:34px;color:var(--navy)}
.services-rule{left:577px;top:1742px}
.service{top:1790px;width:370px;height:212px}
.service.bordered{border-right:1px dashed #9fb5d8}
.service svg{position:absolute;left:22px;top:16px}
.service h3{position:absolute;left:84px;top:14px;font-size:17px;line-height:22px;color:var(--navy);width:280px}
.service p{position:absolute;left:84px;width:280px;font-size:12px;line-height:17px;color:#8a8a8a}
.service a{position:absolute;left:84px;font-size:15px;font-weight:700;color:var(--blue);text-decoration:none}

/* qa */
.qa-media{left:0;top:2099px;width:594px;height:457px;background:linear-gradient(110deg,#4a5e78 0%,#8a8b86 45%,#c5a88e 65%,#6a6f6c 100%)}
.qa-frame{left:18px;top:2134px;width:553px;height:388px;border:1px solid rgba(255,255,255,.85)}
.qa-panel{left:594px;top:2099px;width:606px;height:457px;background:linear-gradient(135deg,#0f3770 0%,#1b4a8c 50%,#0d2c5c 100%)}
.qa-title{left:739px;top:2186px;font-size:33px;color:#fff}
.qa-rule{left:741px;top:2244px;width:44px;height:3px;background:#fff}
.qa-text{left:741px;top:2273px;width:388px;font-size:12.5px;line-height:21px;color:#e5ecf7}
.btn-learn{left:741px;top:2420px;width:177px;height:48px;background:#fff;color:var(--blue);font-family:'Raleway',sans-serif;font-size:15px;font-weight:600;display:flex;align-items:center;justify-content:center}

/* testimonials */
.clients-band{left:0;top:2556px;width:1200px;height:636px;background:linear-gradient(180deg,#3c6ea8 0%,#4e77a6 55%,#7a8aa0 100%)}
.clients-title{left:0;top:2630px;width:1200px;text-align:center;font-size:34px;color:#fff}
.clients-rule{left:577px;top:2685px;width:46px;height:3px;background:#fff}
.card{left:207px;top:2743px;width:784px;height:381px;background:#fff}
.card-photo{left:232px;top:2756px;width:332px;height:353px;background:linear-gradient(160deg,#d8dbdc 0%,#a7a9a6 45%,#5f5a58 80%,#8d8883 100%)}
.card-mark{left:588px;top:2765px;font-family:'Raleway',sans-serif;font-size:110px;color:#eee;line-height:1}
.card-quote{left:600px;top:2815px;width:340px;font-size:12.5px;line-height:21px;color:#777}
.card-divider{left:586px;top:2984px;width:380px;height:1px;background:#e2e2e2}
.card-avatar{left:748px;top:2998px;width:60px;height:60px;border-radius:50%;background:linear-gradient(160deg,#c9b7a8,#6e5a4d);border:3px solid #b43a3a}
.card-name{left:680px;top:3066px;width:196px;text-align:center;font-size:14px;color:var(--blue);font-weight:600}
.card-role{left:680px;top:3090px;width:196px;text-align:center;font-size:10px;color:#5b7fb8}
.card-pager{left:912px;top:3096px}

/* footer */
.footer-band{left:0;top:3192px;width:1200px;height:409px;background:linear-gradient(180deg,#1d4f92 0%,#245aa0 40%,#4670ac 100%)}
.f-brand{left:160px;top:3320px;display:flex;align-items:center;gap:8px}
.f-dot{width:22px;height:22px;border-radius:50%;border:3px solid #fff;display:block}
.f-name{font-family:'Raleway',sans-serif;font-size:23px;color:#fff}
.f-tag{left:186px;top:3351px;font-size:7px;color:#dce6f4}
.f-about{left:160px;top:3381px;width:265px;font-size:12px;line-height:17px;color:#e6eef9}
.f-more{left:162px;top:3483px;font-size:13px;font-weight:700;color:#fff}
.f-col h4{font-size:17px;color:#fff;font-weight:600;margin-bottom:10px}
.f-col li{list-style:none;font-size:12.5px;color:#e6eef9;line-height:26px}
.f-contact li{display:flex;align-items:flex-start;gap:6px}
.subscribe{left:748px;top:3465px;display:flex}
.subscribe-field{width:216px;height:35px;background:#fff;font-size:11px;color:#bbb;padding:10px}
.subscribe-go{width:85px;height:35px;background:var(--navy);color:#fff;font-size:12px;display:flex;align-items:center;justify-content:center}
.socials{left:748px;top:3517px;display:flex;gap:12px}
.socials span{width:24px;height:24px;border-radius:50%;background:#fff;display:block}
.copyright{left:0;top:3601px;width:1200px;height:59px;background:var(--red);color:#fff;font-size:12px;display:flex;align-items:center;justify-content:center}
</style>
</head>
<body>

<!-- hero -->
<div class="abs hero-media" role="img" aria-label="Photo of hands sketching charts on paper beside a laptop"></div>
<div class="abs topbar">
  <div class="abs topbar-contact">✉ info@ledgerwisereach.example &nbsp; ☎ (+123)-555-0147</div>
  <div class="abs topbar-search">
    <svg width="18" height="18" viewBox="0 0 18 18"><circle cx="7.5" cy="7.5" r="5.5" fill="none" stroke="#fff" stroke-width="2"/><line x1="11.5" y1="11.5" x2="16" y2="16" stroke="#fff" stroke-width="2"/></svg>
  </div>
</div>
<div class="abs brand"><span class="brand-dot"></span><span class="brand-name">ledgerwisereach</span></div>
<div class="abs brand-tag">The Demand Generation Company</div>
<nav class="abs nav"><span>Home</span><span>About Us</span><span>Our Services</span><span>Prospora &amp; QA Technology</span><span>Intent Data</span><span>Testimonials</span><span>Contact Us</span></nav>
<div class="abs hero-kicker">WE OFFERS</div>
<h1 class="abs hero-title">MULTI-CHANNEL<br>DEMAND GENERATION SERVICES</h1>
<div class="abs btn-explore">EXPLORE NOW</div>

<!-- updates -->
<div class="abs updates">
  <div class="abs updates-label">LATEST UPDATES</div>
  <div class="abs updates-msg">COVID-19 Service Continuation - New &amp; existing projects to continue as scheduled. <b>click here to read about.</b></div>
  <div class="abs updates-arrows">
    <svg width="30" height="46" viewBox="0 0 30 46"><polyline points="26,3 4,23 26,43" fill="none" stroke="#e59a9a" stroke-width="2"/></svg>
    <svg width="30" height="46" viewBox="0 0 30 46"><polyline points="4,3 26,23 4,43" fill="none" stroke="#e59a9a" stroke-width="2"/></svg>
  </div>
</div>

<!-- partners -->
<div class="abs partners">
  <div class="abs partner-row">
    <div class="partner"><i></i>QRT</div>
    <div class="partner"><i></i>Tarvo</div>
    <div class="partner"><i></i>VKD</div>
    <div class="partner"><i></i>Halvren</div>
    <div class="partner"><i></i>Corvanta</div>
    <div class="partner"><i></i>Mellquist</div>
  </div>
</div>

<div class="abs stats">
  <div class="stat"><div class="stat-label">Downloads Per Month</div><div class="stat-num">70,000+</div></div>
  <div class="stat"><div class="stat-label">Leads Delivered Per Month</div><div class="stat-num">25,000+</div></div>
  <div class="stat"><div class="stat-label">Countries We Can Reach</div><div class="stat-num">50+</div></div>
</div>

<!-- welcome -->
<h2 class="abs welcome-title">WELCOME TO</h2>
<div class="abs rule-red welcome-rule"></div>
<p class="abs welcome-text">Ledgerwise Reach offers multi-channel demand generation services to publishers and technology vendors through our network of lead generation websites and native speaking telemarketing agents. Whether looking for MQL, ABM or BANT campaigns, Ledgerwise Reach can assist you in delivering your demand generation strategy and generate pipeline for your sales teams and/or channel partners.</p>
<div class="abs welcome-frame-out"></div>
<div class="abs welcome-media" role="img" aria-label="Video still of a team working at a wooden table with notebooks"></div>
<div class="abs welcome-frame-in"></div>
<svg class="abs welcome-play" width="62" height="62" viewBox="0 0 62 62"><circle cx="31" cy="31" r="29" fill="rgba(255,255,255,.15)" stroke="#1d57a8" stroke-width="3"/><polygon points="25,19 44,31 25,43" fill="none" stroke="#1d57a8" stroke-width="3"/></svg>

<!-- services -->
<h2 class="abs services-title">OUR SERVICES</h2>
<div class="abs rule-red services-rule"></div>
<div class="abs service bordered" style="left:0">
  <svg width="48" height="50" viewBox="0 0 48 50" fill="none" stroke="#b01f21" stroke-width="2"><rect x="3" y="36" width="7" height="10"/><rect x="18" y="28" width="7" height="18"/><rect x="33" y="20" width="7" height="26"/><polyline points="3,28 18,16 28,22 44,6"/><polyline points="36,6 44,6 44,14"/></svg>
  <h3>MARKETING QUALIFIED LEADS (MQL)</h3>
  <p style="top:72px">A Marketing Qualified Lead (MQL) is a prospect that has expressed an interest in what your brand has to offer. An MQL has taken the first steps to becoming a customer and is ready to receive additional contact from your company.</p>
  <a style="top:168px">Learn More...</a>
</div>
<div class="abs service bordered" style="left:397px">
  <svg width="48" height="50" viewBox="0 0 48 50" fill="none" stroke="#b01f21" stroke-width="2"><rect x="8" y="4" width="30" height="40"/><circle cx="14" cy="22" r="7"/><line x1="24" y1="14" x2="34" y2="14"/><line x1="24" y1="22" x2="34" y2="22"/><line x1="12" y1="32" x2="34" y2="32"/><line x1="12" y1="38" x2="34" y2="38"/></svg>
  <h3>ACCOUNT BASED MARKETING LEADS (ABM)</h3>
  <p style="top:94px">ABM is a strategy that directs marketing resources to engaging a specific set of target accounts.</p>
  <a style="top:168px">Learn More...</a>
</div>
<div class="abs service" style="left:789px">
  <svg width="50" height="50" viewBox="0 0 50 50" fill="none" stroke="#b01f21" stroke-width="2"><path d="M26 4 L46 4 L46 24 L24 46 L4 26 Z"/><circle cx="38" cy="12" r="3"/><circle cx="20" cy="22" r="3"/><circle cx="30" cy="32" r="3"/><line x1="32" y1="18" x2="18" y2="36"/></svg>
  <h3 style="top:32px">SALES QUALIFIED LEAD / BANT</h3>
  <p style="top:86px">An SQL lead or a BANT lead is a type of lead that expressed a specific interest in a product and service that you have to offer...</p>
  <a style="top:166px">Learn More...</a>
</div>

<!-- qa -->
<div class="abs qa-media" role="img" aria-label="Photo of a young man writing on a glass board"></div>
<div class="abs qa-frame"></div>
<div class="abs qa-panel"></div>
<h2 class="abs qa-title">QA TECHNOLOGY</h2>
<div class="abs qa-rule"></div>
<p class="abs qa-text">Prospora is a proprietary lead verification platform from Ledgerwise Reach that aims to sift out invalid leads with questionable or erroneous data. The platform is designed to equip sales teams with accurate, high-quality records in order to improve lead generation, accelerate pipeline and increase revenue.</p>
<div class="abs btn-learn">LEARN MORE</div>

<!-- testimonials -->
<div class="abs clients-band"></div>
<h2 class="abs clients-title">WHAT OUR CLIENTS SAY</h2>
<div class="abs clients-rule"></div>
<div class="abs card"></div>
<div class="abs card-photo" role="img" aria-label="Photo of three colleagues celebrating in an office kitchen"></div>
<div class="abs card-mark">“</div>
<p class="abs card-quote">Lorem Ipsum is simply dummy text of the printing and typesetting industry. Lorem Ipsum has been the industry's standard dummy text ever since the 1500s, when an unknown printer took a galley of type and scrambled it to make a type specimen book.</p>
<div class="abs card-divider"></div>
<div class="abs card-avatar" role="img" aria-label="Portrait of the client"></div>
<div class="abs card-name">Dorian Pelk</div>
<div class="abs card-role">Marketing Head</div>
<svg class="abs card-pager" width="54" height="14" viewBox="0 0 54 14" fill="none" stroke="#888" stroke-width="1.5"><polyline points="8,2 2,7 8,12"/><line x1="2" y1="7" x2="20" y2="7"/><polyline points="46,2 52,7 46,12"/><line x1="34" y1="7" x2="52" y2="7"/></svg>

<!-- footer -->
<footer>
  <div class="abs footer-band"></div>
  <div class="abs f-brand"><span class="f-dot"></span><span class="f-name">ledgerwisereach</span></div>
  <div class="abs f-tag">The Demand Generation Company</div>
  <p class="abs f-about">Ledgerwise Reach offers multi-channel demand generation services to publishers and technology vendors through our network of lead generation websites and native speaking telemarketing agents.</p>
  <div class="abs f-more">Learn More ...</div>
  <div class="abs f-col" style="left:464px;top:3323px"><h4>Quick Links</h4><ul><li>Home</li><li>About Us</li><li>Our Services</li><li>Intent Data</li></ul></div>
  <div class="abs f-col" style="left:617px;top:3323px"><h4>Support</h4><ul><li>Forum Support</li><li>Help &amp; FAQ</li><li>Contact Us</li></ul></div>
  <div class="abs f-col f-contact" style="left:746px;top:3323px"><h4>Contact Info</h4>
    <ul>
      <li style="line-height:15px;margin-top:6px"><svg width="14" height="16" viewBox="0 0 14 16"><path d="M7 1a5 5 0 0 1 5 5c0 4-5 9-5 9S2 10 2 6a5 5 0 0 1 5-5z" fill="#fff"/><circle cx="7" cy="6" r="2" fill="#245aa0"/></svg><span>14 Wrenfold Street #<br>&nbsp;&nbsp;2 Calder Bay, CA 741</span></li>
      <li><svg width="14" height="14" viewBox="0 0 14 14" style="margin-top:6px"><circle cx="7" cy="7" r="7" fill="#fff"/><rect x="3" y="4.5" width="8" height="5" fill="none" stroke="#245aa0"/></svg>info@ledgerwisereach.example</li>
      <li><svg width="14" height="14" viewBox="0 0 14 14" style="margin-top:6px"><circle cx="7" cy="7" r="7" fill="#fff"/><path d="M4.5 3.5l2 2-1 1a5 5 0 0 0 2 2l1-1 2 2-1 1.2C6.5 10.5 3.5 7.5 3.3 4.5z" fill="#245aa0"/></svg>(+123)-555-0147</li>
    </ul>
  </div>
  <div class="abs subscribe"><div class="subscribe-field">Enter your Email...</div><div class="subscribe-go">SUBSCRIBE</div></div>
  <div class="abs socials"><span></span><span></span><span></span><span></span></div>
  <div class="abs copyright">© 2020 Ledgerwise Reach. All Rights Reserved.</div>
</footer>

</body>
</html>
```